church invitation for new individuals or families have moved into our area.

postcard inspiring people to attend our church and the benefits they will receive.
example: make new friends, become closer to God, like minded people, etc.
church info:
Bellwood Fellowship Baptist Church
4417 Co. Rd. 52
Ashford, MO 64790
Sunday school 10:00am
Worship 11:00am
need small map in lower right or left corner

Target Market(s)

new movers into our area

Industry/Entity Type

Church

Font styles to use
Decorative

Colors

Designer to choose colors to be used in the design.

Requirements
Must have
• Inspiring text message that will inspire individuals or families to drive 7 miles east of Carthage to attend our church. graphics ok if designer thinks necessary.
• use both sides of postcard except mail address area.
Nice to have
• You've found your home come and visit ours. God is not concerned about your past flops, failures or fumbles.
Should not have
• message should not sound like someone selling real estate, cars or merchandise.

```html
<!DOCTYPE html>
<html lang="en">
<head>
<meta charset="utf-8">
<title>Bellwood Fellowship Baptist Church – Postcard</title>
<link href="https://fonts.googleapis.com/css2?family=Roboto+Condensed:wght@300;400&family=Norican&display=swap" rel="stylesheet">
<style>
  :root {
    --page-bg: #ecebe8;
    --parchment-light: #f6ecd2;
    --parchment-mid: #ecd7a9;
    --parchment-deep: #ddb878;
    --gold-band: #efcb86;
    --ink: #141414;
    --paper: #ffffff;
    --photo-warm: #d9b48f;
    --map-land: #e6e8e3;
    --label-ink: #555555;
    --frame-line: #b9b9b9;
  }
  html, body {
    margin: 0;
    padding: 0;
    width: 823px;
    height: 1200px;
    overflow: hidden;
    background: var(--page-bg);
  }
  .canvas {
    position: relative;
    width: 823px;
    height: 1200px;
  }
  .postcard {
    position: absolute;
    left: 98px;
    width: 643px;
    height: 495px;
    box-shadow: 0 6px 14px rgba(0,0,0,0.22);
    background: var(--paper);
  }
  .postcard--front { top: 77px; }
  .postcard--back  { top: 631px; }
  .postcard svg { display: block; width: 643px; height: 495px; }
  .church-name { font-family: "Roboto Condensed", sans-serif; font-weight: 300; fill: var(--ink); }
  .headline { font-family: "Roboto Condensed", sans-serif; font-weight: 400; fill: var(--ink); }
  .body-copy { font-family: "Roboto Condensed", sans-serif; font-weight: 300; fill: var(--ink); }
  .script { font-family: "Norican", cursive; fill: var(--ink); }
  .address { font-family: "Roboto Condensed", sans-serif; font-weight: 400; fill: var(--ink); }
  .mail-label { font-family: "Roboto Condensed", sans-serif; font-weight: 300; fill: var(--label-ink); }
</style>
</head>
<body>
<main class="canvas">

  <section class="postcard postcard--front">
    <svg viewBox="0 0 643 495" xmlns="http://www.w3.org/2000/svg">
      <defs>
        <linearGradient id="parchment-front" x1="0" y1="0" x2="1" y2="1">
          <stop offset="0" stop-color="var(--parchment-mid)"/>
          <stop offset="0.45" stop-color="var(--parchment-light)"/>
          <stop offset="1" stop-color="var(--parchment-deep)"/>
        </linearGradient>
        <linearGradient id="photo-tones" x1="0" y1="0" x2="1" y2="1">
          <stop offset="0" stop-color="var(--photo-warm)"/>
          <stop offset="0.55" stop-color="#c99b78"/>
          <stop offset="1" stop-color="#9fbfd9"/>
        </linearGradient>
      </defs>

      <rect class="parchment-panel" width="643" height="495" fill="url(#parchment-front)"/>

      <path class="photo-frame" d="M342 0 Q212 248 342 495 L643 495 L643 0 Z" fill="var(--paper)"/>
      <path class="family-photo" role="img" aria-label="Photo of a smiling family of four outdoors in warm sunlight"
            d="M352 0 Q224 248 352 495 L643 495 L643 0 Z" fill="url(#photo-tones)"/>

      <text class="church-name" x="135" y="55" font-size="27" text-anchor="middle">Bellwood Fellowship</text>
      <text class="church-name" x="135" y="89" font-size="27" text-anchor="middle">Baptist Church</text>

      <text class="headline" x="23" y="177" font-size="62">YOU’RE</text>
      <text class="headline" x="23" y="249" font-size="72">IVITED!</text>

      <line class="divider" x1="24" y1="264" x2="238" y2="264" stroke="var(--ink)" stroke-width="3"/>
      <circle cx="240" cy="264" r="3" fill="var(--ink)"/>

      <g class="body-copy" font-size="14.5" text-anchor="middle">
        <text x="131" y="299">You've found your home</text>
        <text x="131" y="318">come and visit ours.</text>
        <text x="131" y="338">God is not concerned about your</text>
        <text x="131" y="357">past flops, failures or fumbles.</text>
      </g>

      <g class="script" font-size="17.5" text-anchor="middle">
        <text x="131" y="394">Make new friends,</text>
        <text x="131" y="416">Become closer to God,</text>
        <text x="131" y="438">Like minded people</text>
      </g>

      <g class="location-pin" transform="translate(18 460)" fill="var(--ink)">
        <path d="M5.5 0 C2.5 0 0 2.4 0 5.4 C0 9.4 5.5 14 5.5 14 C5.5 14 11 9.4 11 5.4 C11 2.4 8.5 0 5.5 0 Z M5.5 7.6 A2.2 2.2 0 1 1 5.5 3.2 A2.2 2.2 0 1 1 5.5 7.6 Z"/>
      </g>
      <text class="address" x="35" y="473" font-size="15">4417 Co. Rd. 52 Ashford, MO 64790</text>
    </svg>
  </section>

  <section class="postcard postcard--back">
    <svg viewBox="0 0 643 495" xmlns="http://www.w3.org/2000/svg">
      <defs>
        <linearGradient id="parchment-back" x1="0" y1="0" x2="1" y2="1">
          <stop offset="0" stop-color="var(--parchment-deep)"/>
          <stop offset="0.4" stop-color="var(--parchment-light)"/>
          <stop offset="1" stop-color="var(--parchment-deep)"/>
        </linearGradient>
        <clipPath id="parchment-shape">
          <path d="M0 0 L302 0 Q430 248 302 495 L0 495 Z"/>
        </clipPath>
      </defs>

      <rect class="mailing-side" width="643" height="495" fill="var(--paper)"/>
      <path class="gold-band" d="M0 0 L318 0 Q446 248 318 495 L0 495 Z" fill="var(--gold-band)"/>
      <path class="parchment-panel" d="M0 0 L302 0 Q430 248 302 495 L0 495 Z" fill="url(#parchment-back)"/>

      <text class="church-name" x="152" y="53" font-size="29" text-anchor="middle">Bellwood Fellowship</text>
      <text class="church-name" x="152" y="89" font-size="29" text-anchor="middle">Baptist Church</text>

      <line class="divider" x1="22" y1="110" x2="308" y2="110" stroke="var(--ink)" stroke-width="3"/>
      <circle cx="310" cy="110" r="3" fill="var(--ink)"/>

      <g class="body-copy" font-size="16" text-anchor="middle">
        <text x="157" y="146">Sunday school 10:00am</text>
        <text x="157" y="174">Worship 11:00am</text>
      </g>

      <g class="location-pin" transform="translate(22 210)" fill="var(--ink)">
        <path d="M6.5 0 C2.9 0 0 2.8 0 6.4 C0 11 6.5 16.5 6.5 16.5 C6.5 16.5 13 11 13 6.4 C13 2.8 10.1 0 6.5 0 Z M6.5 9 A2.6 2.6 0 1 1 6.5 3.8 A2.6 2.6 0 1 1 6.5 9 Z"/>
      </g>
      <text class="address" x="46" y="225" font-size="18">4417 Co. Rd. 52 Ashford, MO 64790</text>

      <g clip-path="url(#parchment-shape)">
        <rect x="0" y="241" width="420" height="168" fill="var(--paper)"/>
        <rect class="area-map" role="img" aria-label="Small road map showing the route east of town to the church"
              x="0" y="244" width="420" height="162" fill="var(--map-land)"/>
      </g>

      <text class="script" x="156" y="449" font-size="27" text-anchor="middle">See you there!</text>

      <g class="mail-label" font-size="9.5">
        <text x="385" y="48">Bellwood Fellowship Baptist Church</text>
        <text x="385" y="62">4417 Co. Rd. 52</text>
        <text x="385" y="76">Ashford, MO 64790</text>
      </g>
      <rect class="stamp-box" x="539" y="27" width="88" height="59" fill="none" stroke="var(--frame-line)" stroke-width="1.5"/>
    </svg>
  </section>

</main>
</body>
</html>
```